4 'Thank you' greetings cards designs

We are a small greetings card publisher and we need designs for a range of 'Thank you' greetings cards and notecards.
This project is for a total of 4 designs.
Please take a look at this board on Moodpinly, to see the kind of thing we are looking for: https://www.moodpinly.example/dorvek481/thank-you-cards/
The cards will be printed at a maximum size of 131mm x 183mm (including a 3mm bleed) so please provide 300dpi CMYK files at this size. Please ensure that any text (or elements of the design that are not part of the bleed) are at least 11mm in from each edge. Also, please note that cards do not have to have a bleed if your design doesn't require it (e.g. a plain white background).
Please provide 2 designs in 'portrait' orientation and 2 in 'landscape'.
Please provide 2 designs that just have the words 'Thank you' and then 2 designs that include your choice of these alternative messages:
Thank you so much
Thanks very much
Thank you very much
Thanks a million
Just to say thank you
A big thank you
A really big thank you
Feel free to use an exclamation mark on a couple of your designs, if you wish!
Other than the above guidelines, everything else is up to you in terms of colours, fonts, shapes, etc. - but please use the Moodpinly board to see the kind of designs we are looking for.
Thank you!

```html
<!DOCTYPE html>
<html lang="en">
<head>
<meta charset="utf-8">
<title>Thank you card – watercolour butterflies</title>
<link rel="stylesheet" href="https://fonts.googleapis.com/css2?family=Kaushan+Script&display=swap">
<style>
  :root {
    --backdrop: #ecebee;
    --card-paper: #f6eef6;
    --card-paper-edge: #f1e2f0;
    --medallion: #ffffff;
    --medallion-ring: #b98ad0;
    --greeting-ink: #b2328f;
    --splash-blue: #5cc4e6;
    --splash-pink: #f2a6d6;
    --splash-peach: #f7b99a;
    --wing-violet: #9a4cc4;
    --wing-magenta: #d965b4;
    --wing-gold: #f5c766;
    --wing-teal: #6fd3cb;
  }

  html, body {
    margin: 0;
    padding: 0;
    width: 1200px;
    height: 912px;
    overflow: hidden;
    background: var(--backdrop);
  }

  .canvas {
    position: relative;
    width: 1200px;
    height: 912px;
  }

  .card {
    position: absolute;
    left: 60px;
    top: 76px;
    width: 1080px;
    height: 760px;
    background: linear-gradient(135deg, var(--card-paper) 0%, #faf6fa 45%, var(--card-paper-edge) 100%);
    box-shadow: 0 10px 30px rgba(60, 40, 60, 0.18);
    overflow: hidden;
  }

  .card-art {
    position: absolute;
    inset: 0;
    width: 100%;
    height: 100%;
  }

  .greeting {
    position: absolute;
    left: 520px;
    top: 380px;
    width: 400px;
    margin: 0;
    transform: translate(-50%, -50%) rotate(-12deg);
    font-family: "Kaushan Script", cursive;
    font-weight: 400;
    color: var(--greeting-ink);
    line-height: 1;
  }

  .greeting-line {
    display: block;
  }

  .greeting-line--first {
    font-size: 100px;
    padding-left: 30px;
  }

  .greeting-line--second {
    font-size: 92px;
    padding-left: 170px;
    margin-top: 6px;
  }
</style>
</head>
<body>
<main class="canvas">
  <article class="card">
    <svg class="card-art" viewBox="0 0 1080 760" xmlns="http://www.w3.org/2000/svg">
      <defs>
        <radialGradient id="splash-blue-fill" cx="50%" cy="50%" r="50%">
          <stop offset="0%" stop-color="var(--splash-blue)" stop-opacity="0.85"/>
          <stop offset="100%" stop-color="var(--splash-blue)" stop-opacity="0"/>
        </radialGradient>
        <radialGradient id="splash-pink-fill" cx="50%" cy="50%" r="50%">
          <stop offset="0%" stop-color="var(--splash-pink)" stop-opacity="0.8"/>
          <stop offset="100%" stop-color="var(--splash-pink)" stop-opacity="0"/>
        </radialGradient>
        <radialGradient id="splash-peach-fill" cx="50%" cy="50%" r="50%">
          <stop offset="0%" stop-color="var(--splash-peach)" stop-opacity="0.75"/>
          <stop offset="100%" stop-color="var(--splash-peach)" stop-opacity="0"/>
        </radialGradient>
        <radialGradient id="wash-violet" cx="50%" cy="50%" r="50%">
          <stop offset="0%" stop-color="var(--wing-gold)" stop-opacity="0.7"/>
          <stop offset="35%" stop-color="var(--wing-magenta)" stop-opacity="0.55"/>
          <stop offset="70%" stop-color="var(--wing-violet)" stop-opacity="0.3"/>
          <stop offset="100%" stop-color="var(--wing-violet)" stop-opacity="0"/>
        </radialGradient>
        <radialGradient id="wash-teal" cx="50%" cy="50%" r="50%">
          <stop offset="0%" stop-color="var(--wing-teal)" stop-opacity="0.7"/>
          <stop offset="100%" stop-color="var(--wing-teal)" stop-opacity="0"/>
        </radialGradient>
        <radialGradient id="wash-pink" cx="50%" cy="50%" r="50%">
          <stop offset="0%" stop-color="var(--wing-magenta)" stop-opacity="0.6"/>
          <stop offset="100%" stop-color="var(--wing-magenta)" stop-opacity="0"/>
        </radialGradient>
      </defs>

      <g class="watercolour-splash" role="img" aria-label="Watercolour paint splashes in blue, pink and peach behind the medallion">
        <ellipse cx="380" cy="560" rx="260" ry="210" fill="url(#splash-blue-fill)"/>
        <ellipse cx="420" cy="170" rx="170" ry="120" fill="url(#splash-blue-fill)" opacity="0.6"/>
        <ellipse cx="780" cy="330" rx="250" ry="210" fill="url(#splash-pink-fill)"/>
        <ellipse cx="700" cy="560" rx="230" ry="170" fill="url(#splash-peach-fill)"/>
        <ellipse cx="880" cy="520" rx="170" ry="140" fill="url(#splash-pink-fill)" opacity="0.7"/>
      </g>

      <g class="butterfly-area butterfly-area--top-right" role="img" aria-label="Large watercolour butterfly in violet, magenta and gold">
        <ellipse cx="760" cy="150" rx="150" ry="130" fill="url(#wash-violet)"/>
      </g>
      <g class="butterfly-area butterfly-area--bottom" role="img" aria-label="Watercolour butterfly in violet and gold below the medallion">
        <ellipse cx="470" cy="680" rx="130" ry="95" fill="url(#wash-violet)"/>
      </g>
      <g class="butterfly-area butterfly-area--right" role="img" aria-label="Small violet watercolour butterflies beside the medallion">
        <ellipse cx="830" cy="420" rx="110" ry="95" fill="url(#wash-violet)" opacity="0.8"/>
      </g>
      <g class="butterfly-area butterfly-area--pink" role="img" aria-label="Small pink watercolour butterfly">
        <ellipse cx="400" cy="140" rx="100" ry="55" fill="url(#wash-pink)"/>
      </g>
      <g class="butterfly-area butterfly-area--teal-left" role="img" aria-label="Teal watercolour butterfly">
        <ellipse cx="220" cy="380" rx="70" ry="95" fill="url(#wash-teal)"/>
      </g>
      <g class="butterfly-area butterfly-area--teal-small" role="img" aria-label="Small teal watercolour butterfly">
        <ellipse cx="640" cy="650" rx="65" ry="40" fill="url(#wash-teal)"/>
      </g>

      <g class="medallion">
        <circle cx="520" cy="380" r="232" fill="var(--medallion)"/>
        <circle cx="520" cy="380" r="220" fill="none" stroke="var(--medallion-ring)" stroke-width="1.5"/>
      </g>
    </svg>

    <h1 class="greeting">
      <span class="greeting-line greeting-line--first">Thank</span>
      <span class="greeting-line greeting-line--second">you</span>
    </h1>
  </article>
</main>
</body>
</html>
```